Lonestar Canopy Services, INC Roof Safety Info Marketing Material

We need a flyer to illustrate roof safety methods we offer with the pictures and descriptions uploaded. We are a Dallas-based commercial roofing company named Lonestar Canopy Services, INC.
We would like to incorporate our dark blues (seen on our website logo). The final design should communicate roof safety and our ability to assess any roof system based on their safety needs.
https://brellwaytops.com/company/about-brellway-tops-inc/

Target Market(s)

Construction industry

Industry/Entity Type

Commercial Roofind

Font styles to use
Serif

```html
<!DOCTYPE html>
<html lang="en">
<head>
<meta charset="utf-8">
<title>Lonestar Canopy Services – Roof Safety Flyer</title>
<link href="https://fonts.googleapis.com/css2?family=Open+Sans:wght@400;600&family=Roboto+Condensed:wght@400;700&display=swap" rel="stylesheet">
<style>
:root{
  --stage:#0b4a9c;
  --navy:#0f3a78;
  --navy-dark:#0b2f63;
  --lime:#c8f035;
  --paper:#ffffff;
  --text-grey:#8a8f96;
  --panel:#f3f4f6;
  --badge-orange:#f58a4b;
  --badge-green:#3fae49;
}
*{margin:0;padding:0;box-sizing:border-box}
html,body{width:1200px;height:844px;overflow:hidden}
body{background:var(--stage);position:relative;font-family:"Open Sans",sans-serif}
.page{position:absolute;top:117px;width:434px;height:569px;background:var(--paper);overflow:hidden}
.page--front{left:165px}
.page--back{left:664px}
.brand{position:absolute;display:flex;align-items:center;gap:6px;font-family:"Roboto Condensed",sans-serif;font-weight:700;font-size:10px;color:var(--navy);letter-spacing:.3px;text-transform:uppercase}
.brand__dot{width:14px;height:14px;border-radius:50%;background:var(--navy)}
.page--front .brand{left:22px;top:34px}
.page--back .brand{left:0;right:0;top:36px;justify-content:center}
.award{position:absolute;display:flex;align-items:center;gap:8px;background:var(--navy);color:#fff;font-family:"Roboto Condensed",sans-serif;font-weight:700;font-size:10px;letter-spacing:.4px;padding:0 10px}
.award__square{width:14px;height:14px;background:#fff}
.page--front .award{left:267px;top:23px;width:167px;height:27px}
.photo{position:absolute;left:0;width:100%}
.page--front .photo{top:73px;height:148px;background:linear-gradient(180deg,#8a97a6 0%,#c9cdd2 30%,#e9eaea 55%,#d6d8d9 100%)}
.title-band{position:absolute;left:0;top:221px;width:100%;height:63px;background:var(--navy);display:flex;align-items:center;justify-content:center}
.title{font-family:"Roboto Condensed",sans-serif;font-weight:400;font-size:28px;color:#fff;letter-spacing:-.3px}
.title em{font-style:normal;font-weight:700;color:var(--lime)}
.intro{position:absolute;left:45px;top:311px;width:340px;font-size:7.2px;line-height:12.3px;color:var(--text-grey)}
.badge-shape{position:absolute}
.badge-shape--rect{width:40px;height:20px;background:var(--badge-orange);border-radius:2px}
.badge-shape--round{width:28px;height:28px;border-radius:50%;border:3px solid var(--badge-green);background:#fff}
.footer{position:absolute;left:0;bottom:0;width:100%;height:49px;background:var(--navy);display:flex;align-items:center;justify-content:center;gap:16px;color:#fff;font-size:6.6px;line-height:10px}
.footer__item{display:flex;align-items:center;gap:8px}
.footer__divider{width:1px;height:30px;background:rgba(255,255,255,.4)}
.footer strong{font-weight:600}
.footer .label{opacity:.75}
.top-band{position:absolute;left:0;top:63px;width:100%;height:18px;background:var(--navy)}
.page--back .photo{top:81px;height:110px;background:linear-gradient(90deg,#c7d64a 0%,#d9e85a 35%,#a9b04b 55%,#e9ecef 75%,#cfd3d8 100%)}
.anchors-title{position:absolute;left:0;right:0;top:226px;text-align:center;font-family:"Roboto Condensed",sans-serif;font-size:18px;color:var(--navy)}
.anchor-list{position:absolute;left:34px;top:267px;width:354px;list-style:none}
.anchor-list li{position:relative;background:var(--panel);font-size:7.2px;line-height:12px;color:var(--text-grey);padding:5px 10px 5px 26px;margin-bottom:15px}
.anchor-list li::before{content:"";position:absolute;left:11px;top:9px;width:4px;height:4px;border-radius:50%;background:var(--navy)}
.anchor-list li.plain{background:transparent}
.page--back .award{left:232px;top:471px;width:167px;height:28px}
</style>
</head>
<body>

<section class="page page--front">
  <div class="brand"><span class="brand__dot"></span>Lonestar Canopy Services, INC</div>
  <div class="award"><span class="award__square"></span>Safety Program Award</div>
  <div class="photo" role="img" aria-label="Three roofers in hi-vis shirts and hard hats walking across a white commercial rooftop"></div>
  <div class="title-band"><h1 class="title">Creating a “<em>Safety First</em>” mindset</h1></div>
  <p class="intro">“Falls are the leading cause of death in the construction industry. Contractors and facility representatives encounter many hazards on the job, including dangers associated with working at great heights with power tools, electricity, noise, and extreme temperatures. A lack of fall protection, damaged fall protection equipment, or improper setup can drastically increase a roofer’s risk of falling. Unless these hazards are mitigated by the property owner or employer, contractors and facility representatives alike are at risk for serious injury or death. At Lonestar Canopy Services, safety is our main priority. Throughout our inspection, our roofing experts assess your building, identifying three main areas of safety protocol. These areas include evidence of rooftop anchorage to provide safe access to your roof, fall protection systems to allow employees and workers to safely operate on your roof, and protection around fall hazards on your rooftop such as skylights, mechanical or ladder areas. Following our inspection, our team will thoroughly review and recommend a fall prevention plan that is tailored to your specific needs. Our goal is to provide you with a system that is safe, OSHA compliant, and easy to use. For more information on how we can ensure the safety of your roof, call us today!”</p>
  <span class="badge-shape badge-shape--rect" style="left:316px;top:488px"></span>
  <span class="badge-shape badge-shape--round" style="left:394px;top:483px"></span>
  <footer class="footer">
    <div class="footer__item">
      <svg width="16" height="16" viewBox="0 0 24 24" fill="none" stroke="#fff" stroke-width="1.6"><path d="M5 3h4l2 5-2.5 1.5a11 11 0 0 0 6 6L16 13l5 2v4a2 2 0 0 1-2 2A16 16 0 0 1 3 5a2 2 0 0 1 2-2z"/></svg>
      <div><span class="label">Office:</span> <strong>(972) 555-0147</strong><br><span class="label">Service:</span> <strong>(972) 555-0182</strong> (24 Hours 7 Days a Week)</div>
    </div>
    <span class="footer__divider"></span>
    <div class="footer__item">
      <svg width="16" height="16" viewBox="0 0 24 24" fill="none" stroke="#fff" stroke-width="1.6"><circle cx="12" cy="13" r="8"/><path d="M12 9v4l3 2M9 2h6"/></svg>
      <div><span class="label">Mon-Fri 8am to 5pm</span><br><strong>24/7 Emergency On Call Service</strong></div>
    </div>
  </footer>
</section>

<section class="page page--back">
  <div class="brand"><span class="brand__dot"></span>Lonestar Canopy Services, INC</div>
  <div class="top-band"></div>
  <div class="photo" role="img" aria-label="Close-up of a hi-vis safety vest, safety glasses and a white hard hat"></div>
  <h2 class="anchors-title">Pertinent info for roof anchors:</h2>
  <ul class="anchor-list">
    <li>The most important thing (fairly new), if there is an accident on a building, the building owner is responsible for that accident. Previously it fell on the property manager.</li>
    <li class="plain">OSHA guidelines outlined it. Anything with mechanical equipment or any work within 15 feet of a building edge over 6 feet off the ground. Either guard rails or roof anchors. Its all dependent on your specific situation which is where we come into play. We can make that assessment.</li>
    <li>Skylights are a fall-hazard to consider. Roof hatches as well.</li>
  </ul>
  <span class="badge-shape badge-shape--round" style="left:46px;top:470px;width:32px;height:32px"></span>
  <span class="badge-shape badge-shape--rect" style="left:114px;top:474px;width:80px;height:24px"></span>
  <div class="award"><span class="award__square"></span>Safety Program Award</div>
  <footer class="footer">
    <div class="footer__item">
      <svg width="16" height="16" viewBox="0 0 24 24" fill="none" stroke="#fff" stroke-width="1.6"><path d="M5 3h4l2 5-2.5 1.5a11 11 0 0 0 6 6L16 13l5 2v4a2 2 0 0 1-2 2A16 16 0 0 1 3 5a2 2 0 0 1 2-2z"/></svg>
      <div><span class="label">Office:</span> <strong>(972) 555-0147</strong><br><span class="label">Service:</span> <strong>(972) 555-0182</strong> (24 Hours 7 Days a Week)</div>
    </div>
    <span class="footer__divider"></span>
    <div class="footer__item">
      <svg width="16" height="16" viewBox="0 0 24 24" fill="none" stroke="#fff" stroke-width="1.6"><circle cx="12" cy="13" r="8"/><path d="M12 9v4l3 2M9 2h6"/></svg>
      <div><span class="label">Mon-Fri 8am to 5pm</span><br><strong>24/7 Emergency On Call Service</strong></div>
    </div>
  </footer>
</section>

</body>
</html>
```